Current wordpress website needs some additions & to be made more user friendly & visually...

Harbour Kinship Carers Network (HKCN) is a volunteer, not-for-profit organisation supporting parents & carers who are trying to support their loved one with a life-threatening eating disorder. We have a website www.hkcn.org.au which is in Wordpress & need to make membership registration & donations more obvious, streamlined, easy & efficient, as well as reducing how 'wordy' the page looks, by making it more visually appealing. Please refer to the look and feel and functionality of www.brightwatersupportcollective.org.au. Please confirm if our site can look and function as per this site.

```html
<!DOCTYPE html>
<html lang="en">
<head>
<meta charset="utf-8">
<title>Harbour Kinship Carers Network</title>
<link href="https://fonts.googleapis.com/css2?family=Raleway:wght@500;600;700&family=Roboto:wght@400;500;700&display=swap" rel="stylesheet">
<style>
:root{
  --purple:#7a1d6c;
  --purple-dark:#5e1454;
  --green:#5aae22;
  --green-dark:#4b9a18;
  --blue:#3c6db2;
  --ink:#222;
  --text:#5a5a5a;
  --muted:#8a8a8a;
  --line:#e3e3e3;
}
*{box-sizing:border-box;margin:0;padding:0}
html,body{width:1200px;height:4038px;overflow:hidden;background:#fff}
body{font-family:"Roboto",sans-serif;color:var(--text);position:relative}
.page{position:relative;width:1200px;height:4038px;overflow:hidden}
.abs{position:absolute}

/* header */
.brand{left:372px;top:10px;display:flex;align-items:center;gap:14px}
.brand-mark{width:70px;height:70px;border-radius:50%;background:var(--purple)}
.brand-name{font-family:"Raleway",sans-serif;font-weight:600;font-size:22px;color:var(--ink)}
.nav-rule{left:141px;top:111px;width:916px;height:1px;background:var(--line)}
.nav{left:141px;top:127px;width:916px;display:flex;justify-content:space-between;font-size:13px;font-weight:700;color:#333}

/* hero */
.hero{left:0;top:155px;width:1200px;height:613px}
.hero-photo{position:absolute;inset:0;background:linear-gradient(100deg,#c9c3b8 0%,#e2ddd4 35%,#d8c9b6 60%,#b9a58c 100%)}
.hero-curve{position:absolute;left:0;top:0}
.hero-title{left:142px;top:340px;font-family:"Raleway",sans-serif;font-weight:700;font-size:64px;letter-spacing:6px;color:#fff}
.hero-lede{left:144px;top:424px;width:360px;font-size:16px;line-height:25px;color:#fff}
.btn-donate{left:144px;top:495px;width:162px;height:41px;background:var(--green);color:#fff;font-size:14px;font-weight:700;display:flex;align-items:center;justify-content:center;gap:6px}
.slider-arrow{width:32px;height:32px;border-radius:50%;background:rgba(60,60,60,.55);display:flex;align-items:center;justify-content:center}

/* welcome */
.side-label{left:-175px;top:950px;width:420px;transform:rotate(-90deg);font-family:"Raleway",sans-serif;font-weight:700;font-size:72px;color:rgba(0,0,0,.06);white-space:nowrap}
.welcome-title{left:0;top:848px;width:1200px;text-align:center;font-family:"Raleway",sans-serif;font-weight:600;font-size:41px;line-height:57px;color:var(--blue)}
.welcome-title .accent{color:var(--green)}
.welcome-copy{left:180px;top:996px;width:840px;text-align:center;font-size:12.5px;line-height:28px;color:var(--text)}
.welcome-copy p+p{margin-top:28px}

/* green band */
.band{left:0;top:1395px}
.video{left:271px;top:1283px;width:658px;height:353px;background:linear-gradient(135deg,#6d6a68,#9a9693 45%,#b8b3ae);display:flex;align-items:center;justify-content:center}
.play{width:58px;height:42px;border-radius:10px;background:#2b2b2b;display:flex;align-items:center;justify-content:center}
.feature{width:220px;text-align:center;color:#fff}
.feature-icon{width:78px;height:78px;margin:0 auto;border:3px solid rgba(255,255,255,.85);border-radius:50%;background:rgba(255,255,255,.12)}
.feature-label{margin-top:26px;font-family:"Raleway",sans-serif;font-weight:700;font-size:22px}
.dots{left:543px;top:1915px;display:flex;gap:9px}
.dots span{width:15px;height:15px;border:2px solid #fff;border-radius:50%}
.dots span.on{background:#fff;box-shadow:inset 0 0 0 3px var(--green)}

/* section headings */
.sec-head{left:0;width:1200px;text-align:center}
.sec-ghost{font-family:"Raleway",sans-serif;font-weight:700;font-size:80px;color:rgba(0,0,0,.06);line-height:1}
.sec-title{position:absolute;left:0;top:12px;width:100%;font-family:"Raleway",sans-serif;font-weight:600;font-size:40px;color:var(--ink)}

/* blog */
.card{width:281px;height:407px;background:#fff;box-shadow:0 1px 6px rgba(0,0,0,.16)}
.card-photo{height:183px;background:linear-gradient(135deg,#9aa3a8,#d9d2c8)}
.card-date{position:absolute;left:14px;top:145px;background:var(--purple);color:#fff;font-size:11px;font-weight:500;padding:4px 9px}
.card-body{padding:22px 20px 0}
.card-title{font-size:17px;line-height:29px;color:var(--ink)}
.card-excerpt{margin-top:12px;font-size:12px;line-height:25px;color:var(--muted);text-align:justify}
.card-more{margin-top:14px;font-size:13px;font-weight:700;color:var(--purple);display:flex;align-items:center;gap:4px}

/* partners */
.partner-copy{left:260px;top:2898px;width:680px;text-align:center;font-size:13px;line-height:22px;color:var(--muted)}
.partner{width:166px;height:80px;background:#fff;box-shadow:0 1px 5px rgba(0,0,0,.14);display:flex;align-items:center;justify-content:center}
.partner-badge{width:110px;height:34px;border-radius:17px;background:#cfcfcf}

/* map */
.map{left:0;top:3158px;width:1200px;height:493px;background:linear-gradient(160deg,#eee9de,#e6e2d6 50%,#ece6da)}
.btn-direction{left:25px;top:3192px;width:179px;height:39px;background:#fff;box-shadow:0 1px 5px rgba(0,0,0,.2);color:var(--purple);font-size:14px;font-weight:700;display:flex;align-items:center;justify-content:center;gap:8px}
.map-card{left:589px;top:3314px;width:301px;height:97px;background:#fff;box-shadow:0 1px 6px rgba(0,0,0,.2);display:flex;gap:12px;padding:10px}
.map-card-photo{width:70px;height:72px;background:linear-gradient(135deg,#7f93a6,#c2ccd4)}
.map-card-text{font-size:13px;line-height:20px;color:#333}

/* footer */
.footer-curve{left:0;top:3490px}
.foot-head{font-size:16px;font-weight:700;color:#fff;text-decoration:underline;text-underline-offset:3px}
.foot-links{list-style:none;margin-top:24px}
.foot-links li{font-size:13px;color:#fff;height:28px;display:flex;gap:24px}
.contact-row{display:flex;gap:18px;align-items:flex-start;color:#fff;font-size:12.5px;line-height:20px}
.contact-ico{width:30px;height:30px;border-radius:50%;background:var(--purple-dark);flex:none;display:flex;align-items:center;justify-content:center}
.foot-lede{font-size:12.5px;line-height:24px;color:#fff}
.field{height:39px;border:1px solid rgba(255,255,255,.7);color:#fff;font-size:11px;padding:12px 14px}
.btn-submit{height:39px;background:var(--green);color:#fff;font-size:15px;font-weight:700;display:flex;align-items:center;justify-content:center}
.foot-rule{left:144px;top:3950px;width:911px;height:1px;background:rgba(255,255,255,.35)}
.copyright{left:144px;top:3984px;font-size:12.5px;color:#fff}
.social{left:932px;top:3977px;display:flex;gap:6px}
.social span{width:27px;height:27px;border:1.5px solid #fff;border-radius:50%}
</style>
</head>
<body>
<div class="page">

  <!-- header -->
  <div class="abs brand"><div class="brand-mark"></div><div class="brand-name">Harbour Kinship Carers Network</div></div>
  <div class="abs nav-rule"></div>
  <nav class="abs nav">
    <span>Home</span><span>About Eating Disorders</span><span>About HKCN</span><span>Family &amp; Carer Wellbeing</span><span>Services &amp; Clinicians</span><span>Skilled Families</span><span>Members</span><span>Support HKCN</span><span>Contact</span>
  </nav>

  <!-- hero -->
  <section class="abs hero">
    <div class="hero-photo" role="img" aria-label="Young girl at a table looking unhappy at a plate of salad and vegetables"></div>
    <svg class="hero-curve" width="1200" height="613" viewBox="0 0 1200 613">
      <path d="M0 472 Q600 640 1200 472 L1200 613 L0 613 Z" fill="#fff"/>
      <path d="M40 500 Q600 680 1150 500 Q600 620 40 500 Z" fill="#7a1d6c"/>
    </svg>
  </section>
  <div class="abs hero-title">HKCN</div>
  <div class="abs hero-lede">Lorem ipsum dolor sit amet, consectetur sit adipiscing sed eiusmod tempor</div>
  <div class="abs btn-donate">DONATE NOW
    <svg width="14" height="14" viewBox="0 0 14 14"><circle cx="7" cy="7" r="7" fill="#fff"/><path d="M5 7h5M8 4.5 10.5 7 8 9.5" stroke="#5aae22" stroke-width="1.8" fill="none"/></svg>
  </div>
  <div class="abs slider-arrow" style="left:67px;top:392px"><svg width="10" height="12"><path d="M7 1 2 6l5 5" stroke="#fff" stroke-width="2" fill="none"/></svg></div>
  <div class="abs slider-arrow" style="left:1100px;top:392px"><svg width="10" height="12"><path d="M3 1l5 5-5 5" stroke="#fff" stroke-width="2" fill="none"/></svg></div>

  <!-- welcome -->
  <div class="abs side-label">ABOUT HKCN</div>
  <h1 class="abs welcome-title">WELCOME TO <span class="accent">HARBOUR KINSHIP</span><br>CARERS NETWORK</h1>
  <div class="abs welcome-copy">
    <p>The Coastal Wellbeing Centre (CWC) and Nourish Recovery Association (NRA) have merged to form Tidewater Recovery Services (TRS). TRS is funded by Harbour State Health. We provide the largest community support and treatment services for individuals and families living with and recovering from eating disorders, their carers and loved ones. By the sharing of recovery wisdom we aim to involve people with a lived experience, carers and family members and loved ones.</p>
    <p>We would like to respectfully acknowledge the Traditional Owners of the land on which Tidewater Recovery Services operate, and Elders past, present and emerging. Honouring the women elders in diverse communities of which we are a part. Celebrating the extraordinary diversity of women's bodies, genders, sexualities, capacities and relationships that we all represent.</p>
  </div>

  <!-- green band -->
  <svg class="abs band" width="1200" height="650" viewBox="0 0 1200 650">
    <defs><linearGradient id="bandFill" x1="0" y1="0" x2="1" y2="1"><stop offset="0" stop-color="#61b42a"/><stop offset="1" stop-color="#4f9e1c"/></linearGradient></defs>
    <path d="M0 48 Q600 -60 1200 48 L1200 517 Q600 770 0 517 Z" fill="url(#bandFill)"/>
  </svg>
  <div class="abs video" role="img" aria-label="Video still of a distressed woman sitting on a grey sofa">
    <div class="play"><svg width="18" height="20"><path d="M2 1 17 10 2 19Z" fill="#fff"/></svg></div>
  </div>
  <div class="abs feature" style="left:117px;top:1722px"><div class="feature-icon" role="img" aria-label="Get involved icon"></div><div class="feature-label">GET INVOLVED</div></div>
  <div class="abs feature" style="left:369px;top:1722px"><div class="feature-icon" role="img" aria-label="How we work icon"></div><div class="feature-label">HOW WE WORK</div></div>
  <div class="abs feature" style="left:620px;top:1722px"><div class="feature-icon" role="img" aria-label="Our services icon"></div><div class="feature-label">OUR SERVICES</div></div>
  <div class="abs feature" style="left:868px;top:1722px"><div class="feature-icon" role="img" aria-label="Our program icon"></div><div class="feature-label">OUR PROGRAM</div></div>
  <div class="abs dots"><span></span><span></span><span class="on"></span><span></span><span></span></div>

  <!-- blog -->
  <div class="abs sec-head" style="top:2132px"><div class="sec-ghost">FROM THE BLOG</div><h2 class="sec-title">FROM THE BLOG</h2></div>

  <article class="abs card" style="left:144px;top:2236px">
    <div class="card-photo" role="img" aria-label="Group of adults in a support meeting"></div>
    <span class="card-date">APRIL 26, 2019</span>
    <div class="card-body">
      <h3 class="card-title" style="font-weight:400">Lorem ipsum dolor consecter adipiscing eiusmod.</h3>
      <p class="card-excerpt">Lorem ipsum dolor sit amet, consecte tur adipiscing elit, sed do eiusmod tempor incididunt ut labore...</p>
      <div class="card-more">READ MORE <svg width="12" height="12"><circle cx="6" cy="6" r="6" fill="#7a1d6c"/><path d="M4 6h4M6.5 4 8.5 6 6.5 8" stroke="#fff" stroke-width="1.5" fill="none"/></svg></div>
    </div>
  </article>
  <article class="abs card" style="left:459px;top:2236px">
    <div class="card-photo" role="img" aria-label="Young woman resting her head beside a fork"></div>
    <span class="card-date">APRIL 26, 2019</span>
    <div class="card-body">
      <h3 class="card-title" style="font-weight:400">Lorem ipsum dolor consecter adipiscing eiusmod.</h3>
      <p class="card-excerpt">Lorem ipsum dolor sit amet, consecte tur adipiscing elit, sed do eiusmod tempor incididunt ut labore...</p>
      <div class="card-more">READ MORE <svg width="12" height="12"><circle cx="6" cy="6" r="6" fill="#7a1d6c"/><path d="M4 6h4M6.5 4 8.5 6 6.5 8" stroke="#fff" stroke-width="1.5" fill="none"/></svg></div>
    </div>
  </article>
  <article class="abs card" style="left:774px;top:2236px">
    <div class="card-photo" role="img" aria-label="Child leaning on a table next to a bowl"></div>
    <span class="card-date">APRIL 26, 2019</span>
    <div class="card-body">
      <h3 class="card-title" style="font-weight:400">Lorem ipsum dolor consecter adipiscing eiusmod.</h3>
      <p class="card-excerpt">Lorem ipsum dolor sit amet, consecte tur adipiscing elit, sed do eiusmod tempor incididunt ut labore...</p>
      <div class="card-more">READ MORE <svg width="12" height="12"><circle cx="6" cy="6" r="6" fill="#7a1d6c"/><path d="M4 6h4M6.5 4 8.5 6 6.5 8" stroke="#fff" stroke-width="1.5" fill="none"/></svg></div>
    </div>
  </article>

  <div class="abs" style="left:144px;top:2748px;width:911px;height:1px;background:#eee"></div>

  <!-- partners -->
  <div class="abs sec-head" style="top:2808px"><div class="sec-ghost">OUR PARTNERS</div><h2 class="sec-title">OUR PARTNERS</h2></div>
  <p class="abs partner-copy">Lorem ipsum dolor sit amet, consectetur adipiscing elit, sed do eiusmod tempor incididunt ut labore et dolore magna aliqua. Ut enim ad minim veniam, quis nostrud exercitation ullamco laboris.</p>
  <div class="abs partner" style="left:146px;top:2980px"><div class="partner-badge"></div></div>
  <div class="abs partner" style="left:332px;top:2980px"><div class="partner-badge"></div></div>
  <div class="abs partner" style="left:517px;top:2980px"><div class="partner-badge"></div></div>
  <div class="abs partner" style="left:704px;top:2980px"><div class="partner-badge"></div></div>
  <div class="abs partner" style="left:889px;top:2980px"><div class="partner-badge"></div></div>

  <!-- map -->
  <div class="abs map" role="img" aria-label="Street map showing the office location"></div>
  <div class="abs btn-direction">GET DIRECTION
    <svg width="14" height="12"><path d="M1 11C2 6 5 4 9 4V1l4 4-4 4V6C6 6 3 7 1 11Z" fill="#7a1d6c"/></svg>
  </div>
  <svg class="abs" style="left:536px;top:3360px" width="24" height="34" viewBox="0 0 24 34"><path d="M12 0C5 0 0 5 0 12c0 9 12 22 12 22s12-13 12-22C24 5 19 0 12 0Z" fill="#e8202a"/><circle cx="12" cy="12" r="5" fill="#fff"/></svg>
  <div class="abs map-card">
    <div class="map-card-photo" role="img" aria-label="Office building exterior"></div>
    <div class="map-card-text">123 Sample Street, New City,<br>Sample State. US.<div style="margin-top:10px">(+1) 123 456 7890</div></div>
  </div>
  <svg class="abs" style="left:848px;top:3369px" width="42" height="42"><path d="M42 0V42H0Z" fill="#7a1d6c"/><path d="M22 36c1-5 4-7 8-7v-3l4 4-4 4v-3c-3 0-6 1-8 5Z" fill="#fff"/></svg>

  <!-- footer -->
  <svg class="abs footer-curve" width="1200" height="548" viewBox="0 0 1200 548">
    <path d="M0 161 Q600 -20 1200 161" stroke="#5aae22" stroke-width="7" fill="none"/>
    <path d="M0 161 Q600 5 1200 161 L1200 548 L0 548 Z" fill="#7a1d6c"/>
  </svg>

  <div class="abs" style="left:144px;top:3694px">
    <div class="foot-head">QUICK LINKS</div>
    <ul class="foot-links">
      <li><span>»</span>Home</li><li><span>»</span>About Us</li><li><span>»</span>Services</li><li><span>»</span>Latest News</li><li><span>»</span>Member</li><li><span>»</span>Contact Us</li>
    </ul>
  </div>

  <div class="abs" style="left:356px;top:3694px;width:250px">
    <div class="foot-head">CONTACT DETAILS</div>
    <div class="contact-row" style="margin-top:22px">
      <span class="contact-ico"><svg width="10" height="14"><path d="M5 0C2 0 0 2 0 5c0 4 5 9 5 9s5-5 5-9C10 2 8 0 5 0Z" fill="#fff"/><circle cx="5" cy="5" r="2" fill="#5e1454"/></svg></span>
      <span>123 Sample Street, Sample City,<br>New State. USA.</span>
    </div>
    <div class="contact-row" style="margin-top:8px">
      <span class="contact-ico"><svg width="13" height="13"><path d="M3 0 5 3 3.5 5C4.5 7 6 8.5 8 9.5L10 8l3 2-1.5 2.5C6 12.5.5 7 .5 1.5Z" fill="#fff"/></svg></span>
      <span style="line-height:30px">(+1) 123 456 7890</span>
    </div>
    <div class="contact-row" style="margin-top:10px">
      <span class="contact-ico"><svg width="9" height="14"><rect x=".5" y=".5" width="8" height="13" rx="1.5" fill="none" stroke="#fff"/><circle cx="4.5" cy="11" r="1" fill="#fff"/></svg></span>
      <span style="line-height:30px">(+1) 888 888 8888</span>
    </div>
    <div class="contact-row" style="margin-top:12px">
      <span class="contact-ico"><svg width="14" height="10"><rect width="14" height="10" rx="1" fill="#fff"/><path d="M0 1l7 5 7-5" stroke="#5e1454" fill="none"/></svg></span>
      <span style="line-height:30px">admin@hkcn.org.au</span>
    </div>
  </div>

  <div class="abs" style="left:653px;top:3694px;width:402px">
    <div class="foot-head">REQUEST A CALL BACK.</div>
    <p class="foot-lede" style="margin-top:22px">Fill out our short feedback form or send us an email and we'll get in touch shortly...</p>
  </div>
  <div class="abs field" style="left:653px;top:3805px;width:195px">Name</div>
  <div class="abs field" style="left:859px;top:3805px;width:196px">Email</div>
  <div class="abs field" style="left:653px;top:3858px;width:195px">Phone No</div>
  <div class="abs btn-submit" style="left:859px;top:3858px;width:196px">SUBMIT</div>

  <div class="abs foot-rule"></div>
  <div class="abs copyright">Copyrights © 2019 Harbour Kinship Carers Network. &nbsp;All Rights Reserved &nbsp; | &nbsp; Privacy Policy.</div>
  <div class="abs social"><span></span><span></span><span></span><span></span></div>

</div>
</body>
</html>
```